Pelterane Aviation - Insurance Brokers - Half page magazine ad.

Half-page ad in an aviation industry magazine promoting our services as an aviation insurance broker. I've attached an example of a pop-up banner we used at a conference recently to give you an idea.

I have attached a copy of the specifications from the publisher. Half-page ad requires:
- 190mm width x 132mm height
- Minimum 300 dpi
- colours in CMYK
- high resolution PDF with fonts embedded

Target Market(s)

Aircraft owners/operators, drone owners/operators, pilots

Font styles to use
Serif

Colors

Designer to choose colors to be used in the design.

Requirements
Must have
• 1. Company logo (attached).
• 2. Contact Details as follows:
• www.qmvaviation.com.au
• (02) 4931 7262
Nice to have
• Maybe a picture of an aircraft/helicopter in the bakground with logo/text etc over the top. But happy to look at alternative design options.

```html
<!DOCTYPE html>
<html lang="en">
<head>
<meta charset="utf-8">
<title>Pelterane Aviation – Specialist Aviation Insurance Brokers</title>
<link rel="stylesheet" href="https://fonts.googleapis.com/css2?family=Montserrat:ital,wght@0,400;0,500;0,700;1,500&display=swap">
<style>
  :root {
    --navy: #1c1f45;
    --red: #d0213f;
    --paper: #f6f6f6;
    --white: #ffffff;
    --sky-top: #a9b2b0;
    --sky-mid: #b9bdbb;
    --sky-low: #dcae9c;
    --craft-dark: #4a2434;
    --craft-grey: #6f6c70;
    --logo-blue: #1b3f8f;
  }
  * { margin: 0; padding: 0; box-sizing: border-box; }
  html, body { width: 1200px; height: 833px; overflow: hidden; background: var(--white); }
  .ad {
    position: relative;
    width: 1200px;
    height: 833px;
    overflow: hidden;
    font-family: "Montserrat", sans-serif;
    color: var(--navy);
  }
  .backdrop { position: absolute; inset: 0; }
  .brand {
    position: absolute;
    left: 44px;
    top: 58px;
    display: flex;
    align-items: center;
    gap: 12px;
  }
  .brand-mark {
    width: 26px;
    height: 26px;
    background: var(--red);
  }
  .brand-name {
    font-weight: 700;
    font-size: 29px;
    color: var(--logo-blue);
    letter-spacing: -0.3px;
  }
  .headline {
    position: absolute;
    left: 434px;
    top: 168px;
    font-weight: 700;
    font-size: 59px;
    line-height: 60px;
    color: var(--navy);
    letter-spacing: 0.3px;
  }
  .tagline {
    position: absolute;
    left: 438px;
    top: 300px;
    font-style: italic;
    font-weight: 500;
    font-size: 24px;
    color: var(--red);
  }
  .service {
    position: absolute;
    font-size: 26px;
    font-weight: 500;
    color: var(--white);
    letter-spacing: 0.3px;
    white-space: nowrap;
  }
  .contact {
    position: absolute;
    top: 770px;
    display: flex;
    align-items: center;
    gap: 8px;
    font-weight: 700;
    font-size: 22px;
    color: var(--white);
  }
  .contact svg { display: block; }
  .contact-phone { left: 562px; }
  .contact-web { left: 775px; font-size: 25px; letter-spacing: 0.4px; }
</style>
</head>
<body>
<div class="ad">
  <svg class="backdrop" width="1200" height="833" viewBox="0 0 1200 833">
    <defs>
      <linearGradient id="sky" x1="0" y1="0" x2="0" y2="1">
        <stop offset="0" stop-color="var(--sky-top)"/>
        <stop offset="0.55" stop-color="var(--sky-mid)"/>
        <stop offset="1" stop-color="var(--sky-low)"/>
      </linearGradient>
      <radialGradient id="craft" cx="0.42" cy="0.55" r="0.55">
        <stop offset="0" stop-color="var(--craft-dark)"/>
        <stop offset="0.5" stop-color="var(--craft-grey)" stop-opacity="0.85"/>
        <stop offset="1" stop-color="var(--craft-grey)" stop-opacity="0"/>
      </radialGradient>
    </defs>
    <rect class="sky-area" width="1200" height="833" fill="url(#sky)"/>
    <ellipse class="photo-area" cx="200" cy="580" rx="300" ry="240" fill="url(#craft)" role="img" aria-label="Photograph of a large maroon and grey helicopter flying toward the viewer with rotors spinning, against a dusk sky with pink clouds"/>
    <path class="top-band" d="M0 0 H1200 V5 Q620 40 0 256 Z" fill="var(--paper)"/>
    <path class="top-rule" d="M0 256 Q620 40 1200 5" fill="none" stroke="var(--red)" stroke-width="3"/>
    <path class="service-panel" d="M520 833 C512 560 760 330 1200 245 V833 Z" fill="var(--navy)"/>
  </svg>

  <div class="brand">
    <span class="brand-mark"></span>
    <span class="brand-name">Pelterane Aviation</span>
  </div>

  <h1 class="headline">Specialist Aviation<br>Insurance Brokers</h1>
  <p class="tagline">your insurance partner</p>

  <span class="service" style="left:774px;top:526px">Fixedwing</span>
  <span class="service" style="left:1001px;top:526px">Rotorwing</span>
  <span class="service" style="left:707px;top:587px">Manufacturing</span>
  <span class="service" style="left:966px;top:587px">Drones</span>
  <span class="service" style="left:661px;top:648px">Loss of Licence</span>
  <span class="service" style="left:909px;top:648px">Personal Accident</span>

  <div class="contact contact-phone">
    <svg width="22" height="22" viewBox="0 0 24 24" aria-hidden="true">
      <path fill="var(--red)" d="M6.6 10.8a15.1 15.1 0 0 0 6.6 6.6l2.2-2.2c.3-.3.7-.4 1-.2 1.1.4 2.3.6 3.6.6.6 0 1 .4 1 1V20c0 .6-.4 1-1 1C10.6 21 3 13.4 3 4c0-.6.4-1 1-1h3.5c.6 0 1 .4 1 1 0 1.3.2 2.5.6 3.6.1.3 0 .7-.2 1z"/>
    </svg>
    <span>(02) 4931 7262</span>
  </div>
  <div class="contact contact-web">
    <svg width="24" height="18" viewBox="0 0 24 18" aria-hidden="true">
      <rect x="0" y="0" width="24" height="18" rx="1.5" fill="var(--red)"/>
      <path d="M1.5 2 L12 10 L22.5 2" fill="none" stroke="var(--navy)" stroke-width="2"/>
    </svg>
    <span>www.qmvaviation.com.au</span>
  </div>
</div>
</body>
</html>
```